I need an effective flyer that "stimulates" and "motivates" parents and students to visit our website and ultimately register for our Specialized High School Test Prep Program. I need the flyer to be attractive and compelling and include our logo, website url, phone number, session info, and ultimately answer the question-why should you register with Brightpath Study Hubs? Please do not include prices

Target Market(s)

Parents and students (7th-8th Grade)

Industry/Entity Type

School

Requirements
Must have
• -Include colors found in logo or contrast
• -website url, phone number
• -relevant and compelling pictures
• -description of program and "call to action" to register soon!
Should not have
• -Do not include prices

```html
<!DOCTYPE html>
<html lang="en">
<head>
<meta charset="utf-8">
<title>Brightpath Study Hubs – 2016 Schedule</title>
<link href="https://fonts.googleapis.com/css2?family=Montserrat:wght@400;600;700&family=Open+Sans:wght@400;700&display=swap" rel="stylesheet">
<style>
  :root {
    --page: #e9e9ec;
    --paper: #ffffff;
    --green: #8dc63f;
    --blue: #1f6db5;
    --navy: #1a5aa0;
    --orange: #f5a21c;
    --ink: #222;
    --white: #ffffff;
  }
  * { box-sizing: border-box; margin: 0; padding: 0; }
  html, body { width: 1200px; height: 1200px; overflow: hidden; background: var(--page); }
  body { font-family: "Open Sans", Arial, sans-serif; }

  .flyer {
    position: absolute; left: 220px; top: 30px;
    width: 760px; height: 1140px;
    background: var(--paper);
    box-shadow: 0 6px 24px rgba(0,0,0,.15);
    overflow: hidden;
  }

  .hero-photo {
    position: absolute; left: 30px; top: 34px; width: 320px; height: 250px;
    background: radial-gradient(circle at 60% 60%, #f1d2c2 0%, #e4e4e6 45%, #f6f6f7 100%);
  }

  .brand { position: absolute; left: 390px; top: 70px; width: 340px; text-align: center; }
  .brand-name {
    display: inline-flex; align-items: center; gap: 10px;
    font-family: "Montserrat", sans-serif; font-weight: 600; font-size: 27px; color: var(--navy);
  }
  .brand-mark { width: 18px; height: 18px; background: var(--green); }
  .brand-url { margin-top: 24px; font-size: 19px; color: var(--ink); }

  .phone-pill {
    margin: 18px auto 0; width: 260px; height: 50px;
    display: flex; align-items: center; border-radius: 8px; overflow: hidden;
    background: var(--orange);
  }
  .phone-icon { width: 58px; height: 50px; background: var(--blue); display: flex; align-items: center; justify-content: center; }
  .phone-number { flex: 1; text-align: center; font-family: "Montserrat", sans-serif; font-weight: 700; font-size: 23px; color: var(--navy); letter-spacing: 1px; }

  .schedule-title {
    position: absolute; left: 40px; top: 306px; width: 700px;
    font-family: "Montserrat", sans-serif; font-weight: 700; font-size: 36px;
    letter-spacing: 22px; color: var(--navy);
    display: flex; justify-content: space-between;
  }

  .columns { position: absolute; left: 0; top: 360px; width: 760px; height: 560px; }
  .columns svg { position: absolute; inset: 0; }

  .session-list { position: absolute; top: 0; width: 360px; color: var(--white); }
  .session-list.green-side { left: 44px; top: 80px; }
  .session-list.blue-side { left: 420px; top: 20px; }
  .session { height: 122px; }
  .session-label {
    display: inline-block; background: var(--white); color: var(--blue);
    font-family: "Montserrat", sans-serif; font-size: 19px; padding: 3px 10px; margin-bottom: 6px;
  }
  .session-detail { font-size: 17px; line-height: 1.3; padding-left: 12px; }

  .program-note {
    position: absolute; left: 60px; top: 945px; width: 640px;
    text-align: center; font-size: 17px; line-height: 1.45; color: var(--ink);
  }
  .program-note strong { display: block; margin-top: 4px; font-size: 18px; }

  .square-row { position: absolute; left: 60px; top: 1092px; width: 640px; display: flex; justify-content: space-between; }
  .square-row span { width: 20px; height: 20px; }
  .sq-blue { background: var(--blue); }
  .sq-green { background: var(--green); }
  .sq-orange { background: var(--orange); }
</style>
</head>
<body>
<main class="flyer">
  <div class="hero-photo" role="img" aria-label="Photo of a hand writing 'Online Testing' on a laptop screen"></div>

  <header class="brand">
    <div class="brand-name"><span class="brand-mark"></span>Brightpath Study Hubs</div>
    <p class="brand-url">www.brightpathstudyhubs.com</p>
    <div class="phone-pill">
      <div class="phone-icon">
        <svg width="30" height="30" viewBox="0 0 30 30" aria-hidden="true">
          <circle cx="15" cy="15" r="13" fill="none" stroke="#fff" stroke-width="2"/>
          <path d="M10 8 l4 0 l1 4 l-2 2 q2 3 4 4 l2 -2 l4 1 l0 4 q-10 0 -13 -13z" fill="#fff"/>
        </svg>
      </div>
      <div class="phone-number">555-014-2368</div>
    </div>
  </header>

  <h1 class="schedule-title"><span>2016</span><span>SCHEDULE</span></h1>

  <section class="columns">
    <svg width="760" height="560" viewBox="0 0 760 560" aria-hidden="true">
      <rect x="0" y="60" width="420" height="500" fill="#8dc63f"/>
      <polygon fill="#1f6db5" points="380,0 760,0 760,560 390,560 390,470 370,450 390,430 390,350 370,330 390,310 390,230 370,210 390,190 390,110 370,90 390,70 390,20"/>
    </svg>

    <div class="session-list green-side">
      <div class="session"><span class="session-label">SHSAT Session 1A:</span>
        <p class="session-detail">Tuesdays 5:00p.m. – 8:00p.m.<br>June 7, 14, 21, 28<br>July 5</p></div>
      <div class="session"><span class="session-label">SHSAT Session 2A:</span>
        <p class="session-detail">Tuesdays 5:00p.m. – 8:00p.m.<br>July 12, 19, 26<br>August 2, 9</p></div>
      <div class="session"><span class="session-label">SHSAT Session 3A:</span>
        <p class="session-detail">Tuesdays 5:00p.m. – 8:00p.m.<br>August 16, 23, 30<br>September 6, 13</p></div>
      <div class="session"><span class="session-label">SHSAT Session 4A:</span>
        <p class="session-detail">Tuesdays 5:00p.m. – 8:00p.m.<br>September 20, 27<br>October 4, 11, 18</p></div>
    </div>

    <div class="session-list blue-side">
      <div class="session"><span class="session-label">SHSAT Session 1B:</span>
        <p class="session-detail">Thursdays 5:00p.m. – 8:00p.m.<br>June 2, 9, 16, 23, 30</p></div>
      <div class="session"><span class="session-label">SHSAT Session 2B:</span>
        <p class="session-detail">Thursdays 5:00p.m. – 8:00p.m.<br>July 7, 14, 21, 28<br>August 4</p></div>
      <div class="session"><span class="session-label">SHSAT Session 3B:</span>
        <p class="session-detail">Thursdays 5:00p.m. – 8:00p.m.<br>August 11, 18, 25<br>September 8, 15</p></div>
      <div class="session"><span class="session-label">SHSAT Session 4B:</span>
        <p class="session-detail">Thursdays 5:00p.m. – 8:00p.m.<br>September 22, 29<br>October 6, 13, 20</p></div>
    </div>
  </section>

  <p class="program-note">Each session consists of five (5) classes totaling 15 hours. To increase students' ability to perform their level best on the SHSAT, we encourage all students to register for a minimum of two sessions.
    <strong>Serious students are encouraged to register for all four sessions in either session A or B.</strong></p>

  <div class="square-row" aria-hidden="true">
    <span class="sq-blue"></span><span class="sq-green"></span><span class="sq-orange"></span><span class="sq-blue"></span>
    <span class="sq-green"></span><span class="sq-orange"></span><span class="sq-green"></span><span class="sq-blue"></span>
    <span class="sq-orange"></span><span class="sq-green"></span><span class="sq-blue"></span>
  </div>
</main>
</body>
</html>
```